Nordavexa - world unique technology for better life - please let them know who am i at first sight

We need a new business card for company which is a provider of unique crystal based technology suitable for all living being. For more information and final design you can use our brochure (our colours are black and blue from brochure).
We use Verdana font

Industry/Entity Type

Business

Contact Information for Business Card

regular dimension

Other font styles liked:
• Verdana

Requirements
Must have
• Logo
• name
• function/position
• phone
• mobile
• e-mail
• adress
Nice to have
• inovative design (technology directed)

```html
<!DOCTYPE html>
<html lang="en">
<head>
<meta charset="utf-8">
<title>Nordavexa Business Card</title>
<link href="https://fonts.googleapis.com/css2?family=Open+Sans:wght@300;400;600;700&display=swap" rel="stylesheet">
<style>
  :root {
    --page-bg: #e9ebed;
    --card-white: #fbfbfb;
    --card-black: #07090b;
    --brand-blue: #2eaad8;
    --brand-blue-light: #4cc3ea;
    --band-text: #0d3448;
    --ink-dark: #2b2d30;
    --ink-mid: #55585c;
    --rule: #8a8d91;
  }
  * { box-sizing: border-box; margin: 0; padding: 0; }
  html, body {
    width: 1200px; height: 858px; overflow: hidden;
    background: var(--page-bg);
    font-family: "Open Sans", Verdana, sans-serif;
  }
  .canvas {
    width: 1200px; height: 858px;
    display: flex; align-items: center; justify-content: center; gap: 40px;
  }
  .card {
    width: 540px; height: 309px; position: relative; overflow: hidden;
    box-shadow: 0 10px 30px rgba(0,0,0,.18);
  }

  /* Front */
  .card-front { background: var(--card-white); }
  .front-logo {
    position: absolute; left: 0; top: 0; width: 270px; height: 261px;
    display: flex; align-items: center; justify-content: center; gap: 10px;
  }
  .logo-dot { width: 34px; height: 34px; border-radius: 50%; background: var(--brand-blue); }
  .logo-name {
    font-weight: 300; font-size: 30px; letter-spacing: 1px;
    color: var(--brand-blue); text-transform: uppercase;
  }
  .divider {
    position: absolute; left: 270px; top: 46px; width: 1px; height: 168px;
    background: var(--rule);
  }
  .identity { position: absolute; left: 296px; top: 48px; }
  .person-name { font-size: 22px; font-weight: 700; color: var(--ink-dark); line-height: 1.15; }
  .person-role { font-size: 13px; color: var(--ink-mid); margin-top: 2px; }
  .contacts { position: absolute; left: 296px; top: 126px; list-style: none; }
  .contact {
    display: flex; align-items: center; gap: 9px;
    font-size: 14px; color: var(--ink-dark); height: 24px;
  }
  .contact-icon {
    width: 17px; height: 17px; background: var(--brand-blue);
    display: flex; align-items: center; justify-content: center;
  }
  .address-band {
    position: absolute; left: 0; bottom: 0; width: 100%; height: 48px;
    background: linear-gradient(180deg, var(--brand-blue-light), var(--brand-blue));
    display: flex; align-items: center; justify-content: center;
    font-size: 15px; color: var(--band-text);
  }

  /* Back */
  .card-back {
    background: radial-gradient(ellipse at 40% 40%, #141a1f 0%, var(--card-black) 70%);
  }
  .back-logo {
    position: absolute; left: 0; top: 86px; width: 100%;
    display: flex; align-items: center; justify-content: center; gap: 14px;
  }
  .back-logo .logo-dot { width: 52px; height: 52px; }
  .back-logo .logo-name { font-size: 44px; letter-spacing: 2px; }
  .back-web {
    position: absolute; left: 0; bottom: 62px; width: 100%;
    display: flex; align-items: center; justify-content: center; gap: 16px;
    font-size: 15px; color: var(--brand-blue);
  }
  .back-web .line { width: 70px; height: 1px; background: var(--brand-blue); }
</style>
</head>
<body>
<main class="canvas">
  <section class="card card-front" aria-label="Business card front">
    <div class="front-logo">
      <span class="logo-dot"></span>
      <span class="logo-name">Nordavexa</span>
    </div>
    <div class="divider"></div>
    <div class="identity">
      <p class="person-name">Employee Name</p>
      <p class="person-role">Employee Position</p>
    </div>
    <ul class="contacts">
      <li class="contact">
        <span class="contact-icon">
          <svg width="11" height="11" viewBox="0 0 12 12"><rect x="3.5" y="1" width="5" height="10" rx="1" fill="none" stroke="#fff" stroke-width="1.3"/><circle cx="6" cy="9.2" r=".7" fill="#fff"/></svg>
        </span>
        + xxx(x) xx xxx xxx
      </li>
      <li class="contact">
        <span class="contact-icon">
          <svg width="11" height="11" viewBox="0 0 12 12"><path d="M2 3c0-1 1-1.5 4-1.5S10 2 10 3v1H8V3H4v1H2z" fill="#fff"/><rect x="2.5" y="5" width="7" height="5.5" rx="1" fill="#fff"/></svg>
        </span>
        +386(0) 42 715 390
      </li>
      <li class="contact">
        <span class="contact-icon">
          <svg width="11" height="11" viewBox="0 0 12 12"><rect x="1" y="3" width="10" height="6.5" fill="none" stroke="#fff" stroke-width="1.2"/><path d="M1 3l5 4 5-4" fill="none" stroke="#fff" stroke-width="1.2"/></svg>
        </span>
        info@nordavexa.eu
      </li>
      <li class="contact">
        <span class="contact-icon">
          <svg width="11" height="11" viewBox="0 0 12 12"><circle cx="6" cy="6" r="4.6" fill="none" stroke="#fff" stroke-width="1.2"/><ellipse cx="6" cy="6" rx="2" ry="4.6" fill="none" stroke="#fff" stroke-width="1"/><path d="M1.4 6h9.2" stroke="#fff" stroke-width="1"/></svg>
        </span>
        www.nordavexa.eu
      </li>
    </ul>
    <div class="address-band">212-218 Larkfield Road, Leeds LS7 3QN, United Kingdom</div>
  </section>

  <section class="card card-back" aria-label="Business card back">
    <div class="back-logo">
      <span class="logo-dot"></span>
      <span class="logo-name">Nordavexa</span>
    </div>
    <div class="back-web">
      <span class="line"></span>
      <span>www.nordavexa.eu</span>
      <span class="line"></span>
    </div>
  </section>
</main>
</body>
</html>
```